Australian Real Estate Sales Consultant needs web design please.

I am a female residential real estate sales consultant for a large australian real estate franchise.
I need a web design for "wordpress" that contains an area that will accommodate my photo and details and company logo.
A large area that contains a feature property where images are on something like a slide show.
Tabs or something similar with images for Selling, Sold, Photography and News where people can look at listings but I do not want people to be able to post a comment.
Reason: Need more designers, may be forced to change to wordpress and offer more money.
Reason: Sorry for the delay, I have been concentrating on another project which I needed completed. I am now able to focus on my web design project and hope to have it all set up in the next 10 days as it is a high priority for me. Thank you for your patience and I will begin providing feedback to your designs shortly. Thanks, Marisha.
Target Market(s)
Potential sellers or purchasers of residential property
Industry/Entity Type
Residential
Requirements
Must have
- Ease of changing property photos and info
Nice to have
- Bright attractive colours

```html
<!DOCTYPE html>
<html lang="en">
<head>
<meta charset="utf-8">
<title>Marisha Hartwell – Sales Consultant</title>
<link rel="stylesheet" href="https://fonts.googleapis.com/css2?family=Questrial&family=Gelasio:wght@400&family=Open+Sans:wght@400;700&display=swap">
<style>
:root{
  --blue-deep:#0b2f66;
  --blue-mid:#1a5cb0;
  --blue-bright:#2a7ad6;
  --blue-frame:#133e7a;
  --nav-bg:#eef0f2;
  --nav-text:#333;
  --nav-active:#1c4f94;
  --page-bg:#f1f1f1;
  --panel-bg:#ffffff;
  --line:#e2e2e2;
  --heading:#333;
  --body-text:#8a8a8a;
  --price-red:#d8322c;
  --footer-red:#d8231f;
  --white:#ffffff;
  --accent-pink:#e0197a;
}
*{box-sizing:border-box;margin:0;padding:0}
html,body{width:885px;height:1200px;overflow:hidden}
body{position:relative;background:var(--page-bg);font-family:"Open Sans",sans-serif}
.abs{position:absolute}

.site-header{left:0;top:0;width:885px;height:513px;
  background:linear-gradient(180deg,var(--blue-deep) 0%,var(--blue-mid) 45%,var(--blue-bright) 62%,var(--blue-mid) 80%,var(--blue-deep) 100%)}
.brand-mark{left:42px;top:34px;width:40px;height:40px;background:var(--accent-pink);border-radius:4px}
.brand-name{left:108px;top:30px;font-family:"Questrial",sans-serif;color:var(--white);font-size:38px;line-height:44px}
.brand-role{left:165px;top:66px;font-family:"Questrial",sans-serif;color:#dfe7f3;font-size:24px;line-height:28px}

.video-cta{left:535px;top:44px;width:307px;height:73px;border-radius:5px;
  background:linear-gradient(180deg,#3a3a3a 0%,#111 55%,#000 100%);border:1px solid #555}
.video-cta .badge{left:12px;top:12px;width:50px;height:50px;border-radius:6px;background:linear-gradient(#ddd,#888)}
.video-cta .badge-name{left:66px;top:2px;font-family:"Questrial",sans-serif;font-size:9px;color:#ddd;display:none}
.video-cta .title{left:78px;top:14px;font-family:"Gelasio",serif;color:var(--white);font-size:18px}
.video-cta .link{left:152px;top:45px;font-family:"Gelasio",serif;color:#e8262a;font-size:15px}

.hero-frame{left:36px;top:128px;width:810px;height:326px;background:var(--blue-frame);border-radius:3px}
.hero-photo{left:42px;top:134px;width:799px;height:313px;
  background:linear-gradient(90deg,#c9b58a 0%,#8d8065 30%,#b7a98c 50%,#4c4038 72%,#c9a47a 100%)}

.main-nav{left:37px;top:465px;width:809px;height:32px;border-radius:4px;
  background:linear-gradient(180deg,#fafafa,var(--nav-bg));display:flex;align-items:center;
  font-family:"Questrial",sans-serif;font-size:12.5px;color:var(--nav-text);letter-spacing:.3px}
.main-nav span{position:absolute;top:9px}
.main-nav .active{color:var(--nav-active)}

.content-panel{left:35px;top:527px;width:810px;height:575px;background:var(--panel-bg);border:1px solid var(--line);border-radius:3px}
.section-title{font-family:"Gelasio",serif;color:var(--heading);font-size:18px}
.round-arrow{width:19px;height:19px;border-radius:50%;background:#fff;border:1px solid #ccc;box-shadow:0 1px 2px rgba(0,0,0,.15)}
.round-arrow svg{display:block;margin:5px auto}

.listing-row{left:52px;top:564px;width:771px;height:223px;border:1px solid var(--line)}
.listing-divider{top:564px;width:1px;height:223px;background:var(--line)}
.listing-photo{width:197px;height:105px;background:linear-gradient(180deg,#3f6b33 0%,#6c8a63 45%,#9aa6a0 70%,#4e7a3c 100%);box-shadow:0 2px 4px rgba(0,0,0,.25)}
.price-tag{width:73px;height:20px;border-radius:6px;background:linear-gradient(#e8534b,var(--price-red));color:#fff;font-family:"Gelasio",serif;font-size:12px;text-align:center;line-height:20px}
.listing-name{width:197px;text-align:center;font-family:"Gelasio",serif;font-size:17px;color:var(--heading)}
.listing-text{width:210px;font-size:9px;line-height:13.5px;color:var(--body-text)}
.listing-button{width:91px;height:23px;border-radius:3px;background:#fff;border:1px solid #ccc;box-shadow:0 1px 3px rgba(0,0,0,.2);
  font-size:7.5px;font-weight:700;color:#444;text-align:center;line-height:22px;letter-spacing:.3px}

.featured-box{left:52px;top:852px;width:775px;height:220px;border-radius:4px;background:linear-gradient(180deg,#fbfbfb,#ececec);border:1px solid #e6e6e6}
.featured-photo{top:866px;width:330px;height:162px;border-radius:4px}
.featured-text{top:1034px;width:330px;font-size:9px;line-height:13.5px;color:#555}

.site-footer{left:0;top:1128px;width:885px;height:72px;background:var(--footer-red)}
.partner{left:36px;top:1147px;width:224px;height:39px;border:2px solid #fff;background:#1d3b78;
  font-family:"Open Sans",sans-serif;font-weight:700;color:#fff;font-size:15px;line-height:35px;padding-left:12px}
.copyright{left:595px;top:1158px;font-size:9.5px;color:#fff}
</style>
</head>
<body>

<header class="site-header abs"></header>
<div class="brand-mark abs"></div>
<div class="brand-name abs">Marisha Hartwell</div>
<div class="brand-role abs">Sales Consultant</div>

<a class="video-cta abs">
  <span class="badge abs"></span>
  <span class="title abs">Newest Homes With Video</span>
  <span class="link abs">Click Here to Watch..</span>
</a>

<div class="hero-frame abs"></div>
<div class="hero-photo abs" role="img" aria-label="Portrait of the sales consultant on a house veranda"></div>

<nav class="main-nav abs">
  <span class="active" style="left:21px">HOME</span>
  <span style="left:95px">BUYING</span>
  <span style="left:178px">SELLING</span>
  <span style="left:258px">CONTACT US</span>
  <span style="left:371px">NEWS</span>
  <span style="left:440px">PHOTOGRAPHY</span>
  <span style="left:567px">ABOUT ME</span>
  <span style="left:669px">VIDEO</span>
</nav>

<main class="content-panel abs"></main>

<h2 class="section-title abs" style="left:52px;top:538px">Properties For Sale</h2>
<div class="round-arrow abs" style="left:778px;top:540px"><svg width="6" height="8"><path d="M5 0L1 4L5 8" fill="none" stroke="#555" stroke-width="1.3"/></svg></div>
<div class="round-arrow abs" style="left:801px;top:540px"><svg width="6" height="8"><path d="M1 0L5 4L1 8" fill="none" stroke="#555" stroke-width="1.3"/></svg></div>

<div class="listing-row abs"></div>
<div class="listing-divider abs" style="left:303px"></div>
<div class="listing-divider abs" style="left:563px"></div>

<div class="listing-photo abs" style="left:78px;top:573px" role="img" aria-label="Two-storey timber house with veranda"></div>
<div class="price-tag abs" style="left:140px;top:668px">$950,000</div>
<div class="listing-name abs" style="left:78px;top:694px">Modern</div>
<p class="listing-text abs" style="left:78px;top:725px">Soluta nobis est eligendi omnis volutas assumen da est, omnise doloresed rep eldusemp. Soluta nobis omnis ....</p>
<div class="listing-button abs" style="left:127px;top:775px">VIEW THE LISTING</div>

<div class="listing-photo abs" style="left:333px;top:573px" role="img" aria-label="Two-storey timber house with veranda"></div>
<div class="price-tag abs" style="left:395px;top:668px">$950,000</div>
<div class="listing-name abs" style="left:333px;top:694px">Traditional</div>
<p class="listing-text abs" style="left:333px;top:725px">Soluta nobis est eligendi omnis volutas assumenda est, omnise doloresed rep eldusemp. Soluta nobis omnis ....</p>
<div class="listing-button abs" style="left:388px;top:775px">VIEW THE LISTING</div>

<div class="listing-photo abs" style="left:594px;top:573px" role="img" aria-label="Two-storey timber house with veranda"></div>
<div class="price-tag abs" style="left:656px;top:668px">$950,000</div>
<div class="listing-name abs" style="left:594px;top:694px">Classic</div>
<p class="listing-text abs" style="left:592px;top:725px">Soluta nobis est eligendi omnis volutas assumenda est, omnise doloresed rep eldusemp. Soluta nobis omnis ....</p>
<div class="listing-button abs" style="left:657px;top:775px">VIEW THE LISTING</div>

<h2 class="section-title abs" style="left:53px;top:826px">Featured Property</h2>
<div class="featured-box abs"></div>
<div class="round-arrow abs" style="left:69px;top:942px"><svg width="6" height="8"><path d="M5 0L1 4L5 8" fill="none" stroke="#555" stroke-width="1.3"/></svg></div>
<div class="round-arrow abs" style="left:792px;top:942px"><svg width="6" height="8"><path d="M1 0L5 4L1 8" fill="none" stroke="#555" stroke-width="1.3"/></svg></div>

<div class="featured-photo abs" style="left:99px;background:linear-gradient(180deg,#3d6e3a 0%,#8fa7b5 35%,#d9d2bd 60%,#4f8a3a 100%)" role="img" aria-label="Cream two-storey family home with front lawn"></div>
<p class="featured-text abs" style="left:102px">Soluta nobis est eligendi omnis volutas assumenda est, omnise doloresed rep eldusemp. Soluta nobis omnis ....</p>

<div class="featured-photo abs" style="left:452px;background:linear-gradient(180deg,#4a7a3d 0%,#6d6560 30%,#cdb8a2 60%,#c9566a 85%,#6d9b45 100%)" role="img" aria-label="Cottage with gabled roof and flower garden"></div>
<p class="featured-text abs" style="left:453px">Soluta nobis est eligendi omnis volutas assumenda est, omnise doloresed rep eldusemp. Soluta nobis omnis ....</p>

<footer class="site-footer abs"></footer>
<div class="partner abs">Coastline Realty</div>
<p class="copyright abs">Copyright @ 2011 MarishaHartwell.com. All Rights Reserved.</p>

</body>
</html>
```